Business Card Design Project

Use our current logo. Clean design.

Industry/Entity Type

Business

Requirements
Must have
• Marisela DUBRANCQ
M. Law
Managing Partner

Alpenvorsa AG
Kornhalmweg 214
CH-3097 Liebefeld

M. +41 79 412 56 27
T. +41 31 928 44 10
F. +41 31 928 44 19

m.dubrancq@alpenvorsa-example.com
www.alpenvorsa-example.com

```html
<!DOCTYPE html>
<html lang="en">
<head>
<meta charset="utf-8">
<title>Alpenvorsa AG – Business Card</title>
<link rel="stylesheet" href="https://fonts.googleapis.com/css2?family=Arimo:wght@400&family=Open+Sans:wght@400&display=swap">
<style>
  :root {
    --backdrop-center: #3a3a3a;
    --backdrop-edge: #000000;
    --card: #ffffff;
    --ink: #111111;
  }
  html, body {
    margin: 0;
    padding: 0;
    width: 1200px;
    height: 1000px;
    overflow: hidden;
  }
  .stage {
    position: relative;
    width: 1200px;
    height: 1000px;
    background: radial-gradient(circle at 50% 50%, var(--backdrop-center) 0%, #161616 45%, var(--backdrop-edge) 80%);
  }
  .card {
    position: absolute;
    width: 645px;
    height: 421px;
    background: var(--card);
    border-radius: 10px;
    color: var(--ink);
  }
  .card--front { left: 136px; top: 50px; }
  .card--back  { left: 422px; top: 530px; }

  .brand-name {
    position: absolute;
    margin: 0;
    font-family: "Arimo", Arial, sans-serif;
    font-weight: 400;
    color: var(--ink);
    letter-spacing: 1px;
    white-space: nowrap;
    transform: translateX(-50%);
  }
  .card--front .brand-name { left: 320px; top: 200px; font-size: 52px; }
  .card--back  .brand-name { left: 183px; top: 190px; font-size: 40px; }

  .web-contact {
    position: absolute;
    left: 0;
    right: 0;
    top: 320px;
    margin: 0;
    text-align: center;
    font-family: "Open Sans", Arial, sans-serif;
    font-size: 19px;
    line-height: 30px;
  }
  .web-contact span { display: block; }

  .details {
    position: absolute;
    left: 384px;
    top: 52px;
    font-family: "Arimo", Arial, sans-serif;
    font-size: 20px;
    line-height: 29px;
  }
  .details p { margin: 0; }
  .details .person  { margin-bottom: 37px; }
  .details .company { margin-bottom: 40px; }
  .details .phones  { font-size: 18px; line-height: 26.5px; }
</style>
</head>
<body>
<main class="stage">
  <section class="card card--front">
    <h1 class="brand-name">ALPENVORSA</h1>
    <p class="web-contact">
      <span class="email">m.dubrancq@alpenvorsa-example.com</span>
      <span class="website">www.alpenvorsa-example.com</span>
    </p>
  </section>

  <section class="card card--back">
    <h2 class="brand-name">ALPENVORSA</h2>
    <div class="details">
      <p class="person">Marisela DUBRANCQ<br>M. Law<br>Managing Partner</p>
      <p class="company">Alpenvorsa AG<br>Kornhalmweg 214<br>CH-3097 Liebefeld</p>
      <p class="phones">M. +41 79 412 56 27<br>T. +41 31 928 44 10<br>F. +41 31 928 44 19</p>
    </div>
  </section>
</main>
</body>
</html>
```